I need three graphics made that will go on walls in a basketball lockerroom

I need three graphics made that will go on a basketball lockerroom wall. Here are the specifics.
Graphic 1 (Size 115" wide by 52" tall, min 150 DPI)
This should be something that displays the acronym for TOLVAR. The main background color should be the teal color attached. Use logos and the other approved colors as needed.
Standards
Intensity
Effort
Grit
Energy
Love
Graphic 2 (Size 88" wide by 52" tall, min 150 DPI)
This one should be on the Navy Blue background color attached
and impactful way say Attitude and Effort
Graphic 3 (Size 100" wide by 18" tall, min 150 DPI)
This goes along the top of the way and needs to say
(THS logo) Stars Lead the Way (Star logo) Tolvar Basketball (THS logo)
All three of these need to feel like they are of the same style. For Graphic #2 I thought something maybe like the attached basketball except use the S Star in the middle and say attitude and effort using the colors .. but I'm open to other ideas

```html
<!DOCTYPE html>
<html lang="en">
<head>
<meta charset="utf-8">
<title>Tolvar Basketball Locker Room Graphics</title>
<link href="https://fonts.googleapis.com/css2?family=Graduate&family=Oswald:wght@500;600&display=swap" rel="stylesheet">
<style>
  :root{
    --page:#bdbdbf;
    --navy:#1c2d5c;
    --navy-deep:#141f45;
    --teal:#1c9aa6;
    --teal-light:#36c0c4;
    --blue:#2250a6;
    --line:#6fc8e0;
    --silver-hi:#f4f6f8;
    --silver-lo:#9aa1ab;
    --ink:#1c2d5c;
    --white:#ffffff;
  }
  *{margin:0;padding:0;box-sizing:border-box}
  html,body{width:1200px;height:1200px;overflow:hidden;background:var(--page)}
  body{position:relative;font-family:"Oswald",sans-serif}
  .panel{position:absolute;overflow:hidden;box-shadow:0 6px 14px rgba(0,0,0,.35)}
  .panel svg.frame{position:absolute;inset:0;width:100%;height:100%}
  .abs{position:absolute}
  .silver{
    background:linear-gradient(180deg,var(--silver-hi) 0%,#c9ced5 45%,var(--silver-lo) 55%,#e3e6ea 100%);
    -webkit-background-clip:text;background-clip:text;color:transparent;
  }
  .mark-text{font-family:"Graduate",serif;color:var(--white);letter-spacing:1px}
  .mark-circle{position:absolute;border-radius:50%;background:var(--navy);border:2px solid var(--teal-light);
    display:flex;align-items:center;justify-content:center;font-family:"Graduate",serif;color:var(--white)}

  /* Header banner */
  .banner{left:100px;top:349px;width:1000px;height:180px;background:var(--navy)}
  .banner .mark-text{top:62px;font-size:34px}
  .banner .left-mark{left:28px}
  .banner .right-mark{right:28px}
  .banner .headline{font-family:"Graduate",serif;font-size:56px;line-height:1;text-align:center;width:260px}
  .banner .subline{font-family:"Graduate",serif;font-size:19px;color:var(--silver-hi);text-align:center;width:260px;letter-spacing:2px}
  .banner .mark-circle{left:450px;top:40px;width:100px;height:100px;font-size:26px}

  /* Acronym wall */
  .acronym{left:40px;top:569px;width:624px;height:282px;background:var(--navy)}
  .acronym .mark-text{left:0;width:100%;top:18px;text-align:center;font-size:34px}
  .acronym .letters{left:60px;top:70px;width:510px;display:flex}
  .acronym .col{flex:1;text-align:center;border-left:1px solid rgba(255,255,255,.35)}
  .acronym .col:first-child{border-left:none}
  .acronym .letter{font-family:"Graduate",serif;font-size:82px;line-height:1.1;display:block}
  .acronym .word{font-weight:600;font-size:15px;color:var(--white);letter-spacing:.5px;display:block;margin-top:6px}
  .bar-text{font-weight:500;color:var(--ink);letter-spacing:2px}
  .acronym .bar-left{left:90px;top:226px;font-size:15px}
  .acronym .bar-right{left:360px;top:226px;font-size:15px}
  .acronym .mark-circle{left:282px;top:212px;width:60px;height:60px;font-size:15px}

  /* Attitude wall */
  .attitude{left:684px;top:569px;width:477px;height:282px;background:linear-gradient(180deg,var(--teal) 0%,#1f74a8 60%,var(--blue) 100%)}
  .attitude .scene{left:0;top:0;width:100%;height:230px;
    background:radial-gradient(ellipse at 75% 35%,rgba(30,90,120,.55),transparent 60%),radial-gradient(ellipse at 30% 70%,rgba(40,70,160,.45),transparent 60%)}
  .attitude .mark-text{left:0;width:100%;top:14px;text-align:center;font-size:28px}
  .attitude .title{left:0;width:100%;text-align:center;font-family:"Graduate",serif;line-height:1}
  .attitude .t1{top:72px;font-size:58px}
  .attitude .t2{top:134px;font-size:17px;color:var(--white);letter-spacing:2px}
  .attitude .t3{top:156px;font-size:58px}
  .attitude .bar-left{left:70px;top:233px;font-size:13px}
  .attitude .bar-right{left:270px;top:233px;font-size:13px}
  .attitude .mark-circle{left:213px;top:220px;width:52px;height:52px;font-size:13px}
</style>
</head>
<body>

<!-- Header banner -->
<section class="panel banner">
  <svg class="frame" viewBox="0 0 1000 180" preserveAspectRatio="none" aria-hidden="true">
    <rect width="1000" height="180" fill="var(--navy)"/>
    <polygon points="0,150 0,180 1000,180 1000,150 840,150 800,178 200,178 160,150" fill="var(--teal)"/>
    <polygon points="0,150 160,150 200,178 0,178" fill="var(--teal)"/>
    <polyline points="110,0 160,130 420,130" fill="none" stroke="var(--white)" stroke-width="2"/>
    <polyline points="890,0 840,130 580,130" fill="none" stroke="var(--white)" stroke-width="2"/>
    <polyline points="160,130 200,160 800,160 840,130" fill="none" stroke="var(--white)" stroke-width="2"/>
  </svg>
  <span class="abs mark-text left-mark">THS</span>
  <span class="abs mark-text right-mark">THS</span>
  <div class="abs" style="left:165px;top:38px">
    <div class="headline silver">STARS</div>
    <div class="subline">LEAD THE WAY</div>
  </div>
  <div class="mark-circle">THS</div>
  <div class="abs" style="left:585px;top:38px">
    <div class="headline silver">TOLVAR</div>
    <div class="subline">BASKETBALL</div>
  </div>
</section>

<!-- Acronym wall -->
<section class="panel acronym">
  <svg class="frame" viewBox="0 0 624 282" preserveAspectRatio="none" aria-hidden="true">
    <defs>
      <linearGradient id="barSilver" x1="0" y1="0" x2="0" y2="1">
        <stop offset="0" stop-color="#f4f6f8"/><stop offset=".5" stop-color="#c3c8cf"/><stop offset="1" stop-color="#e6e9ec"/>
      </linearGradient>
    </defs>
    <rect width="624" height="282" fill="var(--navy)"/>
    <polyline points="20,44 170,44 190,26 434,26 454,44 604,44" fill="none" stroke="var(--line)" stroke-width="1"/>
    <polygon points="0,190 50,250 574,250 624,190 624,282 0,282" fill="var(--teal)"/>
    <polygon points="40,270 584,270 604,282 20,282" fill="var(--navy-deep)"/>
    <polygon points="55,222 575,222 560,250 70,250" fill="url(#barSilver)"/>
    <polyline points="30,200 60,258 564,258 594,200" fill="none" stroke="var(--white)" stroke-width="1.5"/>
  </svg>
  <span class="abs mark-text">THS</span>
  <div class="abs letters">
    <div class="col"><span class="letter silver">T</span><span class="word">STANDARDS</span></div>
    <div class="col"><span class="letter silver">O</span><span class="word">INTENSITY</span></div>
    <div class="col"><span class="letter silver">L</span><span class="word">EFFORT</span></div>
    <div class="col"><span class="letter silver">V</span><span class="word">GRIT</span></div>
    <div class="col"><span class="letter silver">A</span><span class="word">ENERGY</span></div>
    <div class="col"><span class="letter silver">R</span><span class="word">LOVE</span></div>
  </div>
  <span class="abs bar-text bar-left">STARS LEAD THE WAY</span>
  <span class="abs bar-text bar-right">TOLVAR BASKETBALL</span>
  <div class="mark-circle">THS</div>
</section>

<!-- Attitude wall -->
<section class="panel attitude">
  <div class="abs scene" role="img" aria-label="Photo of a basketball player dunking at a hoop in a gym, with a silver dribbling player illustration, tinted teal and blue"></div>
  <svg class="frame" viewBox="0 0 477 282" preserveAspectRatio="none" aria-hidden="true">
    <defs>
      <linearGradient id="barSilver2" x1="0" y1="0" x2="0" y2="1">
        <stop offset="0" stop-color="#f4f6f8"/><stop offset=".5" stop-color="#c3c8cf"/><stop offset="1" stop-color="#e6e9ec"/>
      </linearGradient>
    </defs>
    <polyline points="20,40 150,40 165,26 312,26 327,40 457,40" fill="none" stroke="var(--line)" stroke-width="1"/>
    <polygon points="0,200 40,255 437,255 477,200 477,282 0,282" fill="var(--teal)"/>
    <polygon points="45,230 432,230 420,254 57,254" fill="url(#barSilver2)"/>
    <polyline points="15,205 50,262 427,262 462,205" fill="none" stroke="var(--white)" stroke-width="1.5"/>
  </svg>
  <span class="abs mark-text">THS</span>
  <div class="abs title t1 silver">ATTITUDE</div>
  <div class="abs title t2">AND</div>
  <div class="abs title t3 silver">EFFORT</div>
  <span class="abs bar-text bar-left">STARS LEAD THE WAY</span>
  <span class="abs bar-text bar-right">TOLVAR BASKETBALL</span>
  <div class="mark-circle">THS</div>
</section>

</body>
</html>
```